velmora - business cards

Need business card designs - logo provided - see www.velmora-example.co.nz

Industry/Entity Type

Business

Requirements
Must have
• logo - provided in attachments
• www.velmora-example.co.nz

```html
<!DOCTYPE html>
<html lang="en">
<head>
<meta charset="utf-8">
<title>velmora – business cards</title>
<link rel="stylesheet" href="https://fonts.googleapis.com/css2?family=EB+Garamond:wght@400&family=Varela+Round&display=swap">
<style>
  :root {
    --bg-light: #f1f1f1;
    --bg-dark: #b9b9b9;
    --charcoal: #3a3a3c;
    --charcoal-soft: #4a4a4c;
    --paper: #f7f7f5;
    --orange: #ef6c1f;
    --orange-soft: #f39a5c;
    --ink: #3d3d3f;
  }
  * { box-sizing: border-box; margin: 0; padding: 0; }
  html, body { width: 1200px; height: 787px; overflow: hidden; }
  body {
    background: radial-gradient(ellipse at 50% 35%, var(--bg-light) 0%, #dcdcdc 55%, var(--bg-dark) 100%);
    position: relative;
    font-family: "Varela Round", sans-serif;
  }
  .card {
    position: absolute;
    top: 244px;
    width: 520px;
    height: 300px;
    overflow: hidden;
    background: var(--paper);
    box-shadow: 0 10px 24px rgba(0,0,0,.22);
  }
  .card--front { left: 50px; }
  .card--back { left: 630px; }

  /* front */
  .band { position: absolute; left: 0; width: 100%; overflow: hidden; }
  .band--top { top: 0; height: 92px; background: var(--charcoal); }
  .band--middle { top: 92px; height: 116px; background: var(--paper); display: flex; align-items: center; justify-content: center; }
  .band--bottom { top: 208px; height: 92px; background: var(--orange); }
  .ghost-name {
    position: absolute; left: 50%; transform: translateX(-50%);
    font-size: 96px; line-height: 1; white-space: nowrap;
  }
  .band--top .ghost-name { top: 40px; color: var(--charcoal-soft); }
  .band--bottom .ghost-name { top: -60px; color: var(--orange-soft); opacity: .6; }

  .wordmark { display: flex; align-items: center; gap: 12px; color: var(--ink); }
  .wordmark__dot { width: 26px; height: 26px; border-radius: 50%; background: var(--orange); }
  .wordmark__name { font-size: 50px; line-height: 1; }
  .wordmark--small { position: absolute; top: 18px; right: 22px; gap: 7px; }
  .wordmark--small .wordmark__dot { width: 13px; height: 13px; }
  .wordmark--small .wordmark__name { font-size: 25px; }

  /* back */
  .disc {
    position: absolute; left: -70px; top: -70px;
    width: 400px; height: 400px; border-radius: 50%;
    background: var(--charcoal);
  }
  .corner-arc {
    position: absolute; right: -90px; bottom: -120px;
    width: 260px; height: 260px; border-radius: 50%;
    background: var(--orange-soft);
  }
  .corner-arc::after {
    content: ""; position: absolute; left: 22px; top: 22px;
    width: 260px; height: 260px; border-radius: 50%;
    background: var(--orange);
  }
  .contact {
    position: absolute; left: 54px; top: 84px; color: #fff;
    font-family: "EB Garamond", serif;
  }
  .contact__name { font-size: 30px; letter-spacing: 1px; line-height: 1; }
  .contact__title { font-size: 15px; color: var(--orange); text-align: right; letter-spacing: 1px; margin-top: 4px; }
  .contact__lines { margin-top: 22px; font-size: 14px; line-height: 1.6; letter-spacing: .5px; }
</style>
</head>
<body>
  <section class="card card--front" aria-label="Card front">
    <div class="band band--top"><span class="ghost-name" aria-hidden="true">velmora</span></div>
    <div class="band band--middle">
      <div class="wordmark">
        <span class="wordmark__dot"></span>
        <span class="wordmark__name">velmora</span>
      </div>
    </div>
    <div class="band band--bottom"><span class="ghost-name" aria-hidden="true">velmora</span></div>
  </section>

  <section class="card card--back" aria-label="Card back">
    <div class="corner-arc"></div>
    <div class="disc"></div>
    <div class="wordmark wordmark--small">
      <span class="wordmark__dot"></span>
      <span class="wordmark__name">velmora</span>
    </div>
    <div class="contact">
      <p class="contact__name">MARCUS ELLERY</p>
      <p class="contact__title">TITLE HERE</p>
      <p class="contact__lines">000.000.00000<br>hello@velmora.example<br>www.velmora-example.co.nz</p>
    </div>
  </section>
</body>
</html>
```